Professional business cards for our auto wholesale dealership.

Target Market(s)

New and used cars sales managers and middle class to higher end private party buyers.

Industry/Entity Type

Automotive

Contact Information for Business Card

Bayline Premier Motors
Marcus T Holloway
Owner
(555) 417-3860
baypremmotors@mailbox-example.net
Dealer Lic # 48261

Logo Text

Bayline Premier Motors, Bay Prem Motors, BPM, etc

Font styles to use
Serif
Sans Serif

Colors

Designer to choose colors to be used in the design.

Requirements
Must have
• A professional, but not pretentious, look
Nice to have
• It might be nice to see "BPM" in a shape form i.e. circle, triangle, etc in the corner or background somehwere
Should not have
• bright "girly" colors

```html
<!DOCTYPE html>
<html lang="en">
<head>
<meta charset="utf-8">
<title>Bayline Premier Motors – Business Card</title>
<link rel="stylesheet" href="https://fonts.googleapis.com/css2?family=Open+Sans:wght@400;600;700&display=swap">
<style>
  :root {
    --navy: #1f3a7a;
    --ink: #3a3a3a;
    --muted: #6b6b6b;
    --paper: #f4f4f4;
    --backdrop: #5c5c5c;
    --rule: #4a4a4a;
  }
  * { box-sizing: border-box; margin: 0; padding: 0; }
  html, body { width: 1200px; height: 904px; overflow: hidden; }
  body {
    background: var(--backdrop);
    font-family: "Open Sans", Arial, sans-serif;
    position: relative;
  }
  .card {
    position: absolute;
    width: 560px;
    height: 320px;
    border-radius: 3px;
    box-shadow: 0 10px 24px rgba(0,0,0,0.35);
  }
  .card-front {
    left: 140px;
    top: 80px;
    background: var(--navy);
    display: flex;
    align-items: center;
    justify-content: center;
  }
  .front-mark {
    color: #fff;
    font-weight: 400;
    font-size: 48px;
    letter-spacing: 8px;
  }
  .card-back {
    left: 500px;
    top: 500px;
    background: linear-gradient(135deg, #ffffff 0%, var(--paper) 60%, #e6e6e6 100%);
  }
  .brand {
    position: absolute;
    left: 40px;
    top: 92px;
    width: 220px;
    display: flex;
    flex-direction: column;
    align-items: center;
    gap: 14px;
  }
  .brand-dot {
    width: 64px;
    height: 64px;
    border-radius: 50%;
    background: var(--navy);
  }
  .brand-name {
    color: var(--navy);
    font-weight: 400;
    font-size: 17px;
    letter-spacing: 1.5px;
    text-align: center;
    line-height: 1.3;
    text-transform: uppercase;
  }
  .divider {
    position: absolute;
    left: 285px;
    top: 78px;
    width: 1px;
    height: 150px;
    background: var(--rule);
  }
  .details {
    position: absolute;
    left: 318px;
    top: 78px;
    width: 230px;
  }
  .person-name {
    color: var(--navy);
    font-weight: 700;
    font-size: 20px;
    line-height: 1.2;
  }
  .person-role {
    color: var(--ink);
    font-size: 12px;
    margin: 2px 0 12px 14px;
  }
  .contact-list { list-style: none; }
  .contact-list li {
    display: flex;
    align-items: center;
    gap: 9px;
    color: var(--ink);
    font-size: 11.5px;
    line-height: 1.9;
    white-space: nowrap;
  }
  .contact-list svg { width: 13px; height: 13px; flex: none; }
</style>
</head>
<body>
  <section class="card card-front" aria-label="Card front">
    <span class="front-mark">BPM</span>
  </section>

  <section class="card card-back" aria-label="Card back">
    <div class="brand">
      <span class="brand-dot"></span>
      <span class="brand-name">Bayline Premier Motors</span>
    </div>

    <span class="divider"></span>

    <div class="details">
      <h1 class="person-name">Marcus T Holloway</h1>
      <p class="person-role">Owner</p>
      <ul class="contact-list">
        <li>
          <svg viewBox="0 0 16 16" aria-hidden="true"><path fill="#1f3a7a" d="M3.6 1.5l2.3 2.6-1.3 1.7c.9 2 2.6 3.7 4.6 4.6l1.7-1.3 2.6 2.3-1.5 2.1C7.2 13.4 2.6 8.8 1.5 3z"/></svg>
          (555) 417-3860
        </li>
        <li>
          <svg viewBox="0 0 16 16" aria-hidden="true"><rect x="1.5" y="3.5" width="13" height="9" rx="1" fill="#1f3a7a"/><path d="M2 4.5l6 4.5 6-4.5" stroke="#fff" stroke-width="1.2" fill="none"/></svg>
          baypremmotors@mailbox-example.net
        </li>
        <li>
          <svg viewBox="0 0 16 16" aria-hidden="true"><circle cx="8" cy="8" r="6.5" fill="#1f3a7a"/><path d="M1.5 8h13M8 1.5c-3 3.5-3 9.5 0 13M8 1.5c3 3.5 3 9.5 0 13" stroke="#fff" stroke-width="1" fill="none"/></svg>
          Dealer Lic # 48261
        </li>
      </ul>
    </div>
  </section>
</body>
</html>
```